Wex2Legal Letterhead

Need a new letterhead for my law firm.
IDENTIFYING INFORMATION BELOW:
Teodoro R Galvani III
Attorney at Law
Address: 2834 Brackett Ave, Ste 300, Dallas, TX 75204
Phone: 877-642-7183
Fax: 469-538-2716
Email: ted@wex2legal-example.com
Website: www.wex2legal-example.com

Colors
0054AA
0677BA
7BADD7
CADEEF
E8F1F8

Requirements
Must have
• Logo needs to be on the letterhead, along with identifying information which is included in the project description.

```html
<!DOCTYPE html>
<html lang="en">
<head>
<meta charset="utf-8">
<title>Wex2Legal Letterhead</title>
<link rel="stylesheet" href="https://fonts.googleapis.com/css2?family=Inter:wght@400;500;700&family=Arimo:wght@400&display=swap">
<style>
  :root {
    --backdrop: #aeadae;
    --paper: #ffffff;
    --ink: #111111;
    --body-ink: #555555;
    --brand-blue: #009bd9;
    --on-blue: #ffffff;
    --divider: #009bd9;
    --signature-tone: #d7d9dd;
  }
  * { margin: 0; padding: 0; box-sizing: border-box; }
  html, body {
    width: 1039px; height: 1200px; overflow: hidden;
    background: var(--backdrop);
  }
  .letterhead {
    position: absolute; left: 105px; top: 16px;
    width: 829px; height: 1168px;
    background: var(--paper);
    font-family: "Inter", sans-serif;
    color: var(--ink);
  }
  .brand { position: absolute; left: 68px; top: 92px; width: 244px; text-align: center; }
  .brand-name {
    font-family: "Inter", sans-serif; font-weight: 700;
    font-size: 36px; letter-spacing: 1px; line-height: 38px; color: var(--ink);
  }
  .brand-tagline {
    font-size: 15px; letter-spacing: 2.6px; line-height: 18px; font-weight: 400; color: var(--ink);
  }
  .name-band {
    position: absolute; left: 494px; top: 90px; width: 335px; height: 56px;
    background: var(--brand-blue); color: var(--on-blue);
    text-align: right; padding: 9px 54px 0 0;
  }
  .attorney-name { font-weight: 700; font-size: 20px; line-height: 24px; white-space: nowrap; }
  .attorney-title { font-size: 14px; line-height: 18px; font-weight: 400; }
  .letter {
    position: absolute; left: 62px; top: 390px; width: 700px;
    font-family: "Arimo", sans-serif; color: var(--body-ink);
  }
  .salutation { font-size: 17px; line-height: 24px; margin-bottom: 19px; }
  .letter p { font-size: 12.6px; line-height: 19.6px; text-align: justify; margin-bottom: 19.6px; }
  .letter p.closing { margin-bottom: 0; }
  .signature {
    position: absolute; left: 63px; top: 792px; width: 105px; height: 42px;
    background: linear-gradient(90deg, var(--signature-tone), #eceef0);
    border-radius: 3px;
  }
  .contact-bar { position: absolute; left: 0; top: 1075px; width: 829px; height: 30px; font-size: 13.3px; line-height: 16px; }
  .contact-group { position: absolute; top: 1px; }
  .address { left: 80px; }
  .phones { left: 361px; }
  .web { left: 599px; }
  .contact-line { display: flex; align-items: center; gap: 5px; white-space: nowrap; }
  .contact-line svg { width: 11px; height: 11px; flex: none; }
  .divider { position: absolute; top: 0; width: 1px; height: 27px; background: var(--divider); }
  .divider.first { left: 297px; }
  .divider.second { left: 534px; }
</style>
</head>
<body>
<main class="letterhead">
  <header>
    <div class="brand">
      <div class="brand-name">WEX2LEGAL</div>
      <div class="brand-tagline">LAW MADE CLEAR</div>
    </div>
    <div class="name-band">
      <div class="attorney-name">TEODORO R GALVANI III</div>
      <div class="attorney-title">Attorney at Law</div>
    </div>
  </header>

  <section class="letter">
    <div class="salutation">Dear Mr. Smith,</div>
    <p>Lorem ipsum dolor sit amet, consectetur adipiscing elit. Donec orci purus, luctus vitae dignissim eu, iaculis sed purus. Vivamus faucibus, ipsum nec aliquet viverra, leo mauris condimentum ligula, sit amet sagittis enim ligula quis arcu. Nam egestas tortor id nisi porttitor mattis. In tortor ante, ultricies in suscipit a, tempus non massa. Vivamus et auctor mi. Fusce vel massa nulla. Phasellus nec eros mauris, et scelerisque orci.</p>
    <p>Donec malesuada orci vitae nulla accumsan porta a id massa. Quisque accumsan iaculis magna sit amet fringilla. Maecenas consequat, magna eget tincidunt semper, odio nibh rutrum mi, id feugiat ante nisi eu risus. Vestibulum nunc orci, rhoncus a placerat in, ultricies in mi. Cras mattis varius eros, vel fringilla nisi suscipit eget. Quisque scelerisque sagittis nulla at porttitor.</p>
    <p>Sed id augue vitae urna euismod commodo aliquet a quam. Pellentesque arcu velit, cursus et malesuada ut, consequat et diam. Nullam erat sem, rhoncus id ullamcorper vitae, rhoncus et arcu. In ultricies ultricies nulla, ut rutrum nisi iaculis at. Donec eu magna a metus ornare faucibus. Fusce aliquet faucibus ultricies. Morbi semper, est id tincidunt gravida, sem arcu adipiscing lacus, ac bibendum nulla leo eu purus. Quisque nec diam sed risus consectetur accumsan quis quis nibh. Vestibulum id purus lorem.</p>
    <p class="closing">Sincerely,</p>
  </section>

  <div class="signature" role="img" aria-label="Handwritten signature of the attorney"></div>

  <footer class="contact-bar">
    <div class="contact-group address">
      <div>2834 Brackett Ave</div>
      <div>Ste 300, Dallas, TX 75204</div>
    </div>
    <span class="divider first"></span>
    <div class="contact-group phones">
      <div class="contact-line">
        <svg viewBox="0 0 12 12" aria-hidden="true"><path fill="#009bd9" d="M2.5 1l2 2.2-1 1.3c.7 1.5 1.8 2.6 3.2 3.3l1.3-1L11 8.7 9.7 11C5 10.6 1.4 7 1 2.3z"/></svg>
        <span>877-642-7183</span>
      </div>
      <div class="contact-line">
        <svg viewBox="0 0 12 12" aria-hidden="true"><rect x="3" y="1" width="6" height="3" fill="#009bd9"/><rect x="1" y="4.5" width="10" height="4.5" rx="1" fill="#009bd9"/><rect x="3" y="7.5" width="6" height="3.5" fill="#fff" stroke="#009bd9"/></svg>
        <span>469-538-2716</span>
      </div>
    </div>
    <span class="divider second"></span>
    <div class="contact-group web">
      <div class="contact-line">
        <svg viewBox="0 0 12 12" aria-hidden="true"><rect x="1" y="2.5" width="10" height="7" fill="#009bd9"/><path d="M1 2.5l5 4 5-4" fill="none" stroke="#fff" stroke-width="1"/></svg>
        <span>ted@wex2legal-example.com</span>
      </div>
      <div class="contact-line">
        <svg viewBox="0 0 12 12" aria-hidden="true"><g fill="none" stroke="#009bd9" stroke-width=".9"><circle cx="6" cy="6" r="4.8"/><ellipse cx="6" cy="6" rx="2" ry="4.8"/><path d="M1.2 6h9.6M2 3.5h8M2 8.5h8"/></g></svg>
        <span>www.wex2legal-example.com</span>
      </div>
    </div>
  </footer>
</main>
</body>
</html>
```